Graphic Design Project - Top Ten Tips for Surviving a Tax Investigation Graphic/Infographic

This is a challenging one so I need someone really good to convert this into a useful graphic.

I have some content around top tips for Surviving a Tax Investigation. Not sure if this can be represented in an "infographic" as its not data - centric (more of a top ten list) but i would like some kind of infographic based image to share around my social networks.

The content is as follows - obviously the text will need to be reduced significantly without losing the message and it must allow a link and be branded as Pendrake Tax (www.pendraketax.co.uk)

_________________________________________________

Surviving a Tax Investigation

So what are the key things to do (or not to do).

1. Don’t Panic

For many here will be an initial knee jerk reaction such as fear,denial and anger or a desire to have a chat with the Inspector to show you are a good person and willing to help or to assure BQTF there is nothing wrong.
This is a time for cool heads, planning and contemplation as to what could be the problems and taking stock of the situation. Do not do anything rash and:

2. Take Expert advice

Your fist discussion may be with your accountant. Some are good at tax investigation work, many are not specialists. Engaging a specialist can make all the difference in time taken to deal with the issues and the eventual outcome. You must have an open and honest conversation about what may or may not have gone on and sometimes this is difficult with existing advisors. An expert in the field of tax investigations understands the legal frame work in which BQTF operates and the subtleties of tax investigations which can be used to your advantage. After all you would not ask a GP to conduct specialised surgery.

3. Don’t Lie

Tell your advisor the truth, if you have chosen well then they will be able to manage the situation properly. If there is something wrong then it is best this is disclosed to BQTF at the earliest given opportunity.

4. BQTF already knows quite a lot

BQTF rarely go on ‘fishing expeditions’. Before any tax investigation they review your tax returns and research their ‘data warehouse’ for background information on property and other assets, interest bearing bank accounts and now they have access to various information from Q5 countries including overseas property. Often they will have sufficient evidence to suspect that there are problems with your tax affairs. If you do not tell them and they have to tell you then the costs of sorting the matter out goes up significantly.

5.Think critically

Think about what has gone wrong (if it has) and how it has happened. Before sending anything to BQTF or make sure you it has been looked at and consider if anything needs explanation.
Make sure if any bank statements are sent to BQTF that any none business deposits are explained.

6.Prepare for meetings

If you do attend a meeting make sure you are prepared. Anticipate any questions (this is where an experience advisor really helps) and think about your answers. Never attend without an advisor and ensure you take notes of what was said. Meetings are not just about finding more about the business, they are designed to catch you out.

7. Question what BQTF are asking for

BQTF often ask for things that they are not entitled to or send out onerous requests. Ask them why they need the information and think about what it has to do with your tax affairs. If the answer is it is nothing to do with your tax return then it is unlikely that it should be provided.

8. Deadline Management

BQTF Officers are under tremendous internal pressure to keep Investigations flowing. They will often suggest deadlines for the provision of information and responses. Often these are unreasonable. If you think they are entitled to the information then think about how long it will take you to do as they ask. Then tell them how long you think it will take to do. Remember where there are delays BQTF have unavoidable delays due to pressure of work, you are not cooperating!

9.Make Payments on Account

If you do owe tax then (if you have the funds) you should make payments on account to BQTF.
This demonstrates cooperation with BQTF and stops the clock of further interest accruing from the date the payment is made on the amount of the payment.

10.Find Solutions

At certain points in a tax investigation there will be questions to which no one knows the answer or technical ‘grey’ areas where the answer is unclear. Make pragmatic suggestions to BQTF as to how these could be resolved

11.Mitigate Penalties/Name and Shame

Penalties are based on perceived behaviour so make sure you understand how these work and read BQTF’s own guidance on this. Ensure that all answers to questions support the behaviour that you think has happened and that the penalty mitigation factors have all been covered. The difference between disclosing problems and helping sort them out, or denying them can reduce penalties by a massive margin. Behaviour during the enquiry can also have an influence on whether you appear on the quarterly name and shame list of “tax cheats” or not. Make sure you are not.

12.Don’t Do It Again!

BQTF do not look favourably on second time offenders and at best they will charge you a high penalty and these are always looked at more seriously for prosecution. Tax investigations are such a traumatic experience that most people never want to experience them again.

_________________________________

A draft will need to be submitted show a wireframe and look and feel for review towards the beginning of the project to allow for amends. Estimated 2-3 amends total throughout the life of the project.

Remember this is targeted to the UK market so spelling and grammar need to reflect this

I would like applicants to send me examples of their work. This needs to be highly professional and supplied as illustrator or photoshop files as well as JPG/PNG

Theme = highly professional, serious, on brand, emulating expertise, confident yet friendly- these people are on your side.

The files attached give you an idea of the theme of the brand

finance professionals, customers

Legal

• icons/graphics - should not be all text, needs to be as creative as possible given the content is heavy text

```html
<!DOCTYPE html>
<html lang="en-GB">
<head>
<meta charset="utf-8">
<title>How to survive a Tax Investigation – Pendrake Tax</title>
<link href="https://fonts.googleapis.com/css2?family=Open+Sans:wght@400;600;700;800&family=Roboto:wght@700;900&display=swap" rel="stylesheet">
<style>
  :root{
    --page:#e6eaef;
    --stripe:#dde2e8;
    --white:#ffffff;
    --slate:#4d5d6e;
    --slate-dark:#3a4756;
    --blue:#4a7fb8;
    --blue-dark:#2f5d93;
    --brand:#5b8fc6;
    --text:#3c4450;
    --line:#ffffff;
  }
  *{margin:0;padding:0;box-sizing:border-box}
  html,body{width:1200px;height:3175px;overflow:hidden}
  body{
    position:relative;
    font-family:"Open Sans",Arial,sans-serif;
    color:var(--text);
    background:repeating-linear-gradient(180deg,var(--page) 0 120px,var(--stripe) 120px 240px);
  }
  .masthead{
    position:absolute;left:0;top:0;width:1200px;height:118px;background:var(--white);
    display:flex;align-items:center;justify-content:center;gap:18px;
  }
  .brand-name{font-family:"Open Sans",sans-serif;font-weight:800;font-size:56px;letter-spacing:2px;color:var(--brand);text-transform:uppercase}
  .brand-mark{width:40px;height:40px;background:var(--brand)}
  .title-band{
    position:absolute;left:0;top:118px;width:1200px;height:240px;
    background:linear-gradient(180deg,#5a6b7d,var(--slate-dark));
    display:flex;align-items:center;justify-content:center;text-align:center;
  }
  .title-band h1{
    font-family:"Roboto",sans-serif;font-weight:900;font-size:88px;line-height:1.0;color:var(--white);
    text-shadow:3px 4px 0 rgba(0,0,0,.45);
  }
  .spine{position:absolute;left:597px;top:358px;width:6px;height:2612px;background:var(--line)}
  .photo{position:absolute;border:6px solid var(--white)}
  .photo-kneeling{left:25px;top:378px;width:562px;height:272px;background:linear-gradient(160deg,#f2f4f6,#b9c1c9 70%,#5c636b)}
  .photo-card{left:25px;top:1080px;width:562px;height:272px;background:linear-gradient(150deg,#dfe6ee,#8ea4bb 60%,#2d3a48)}
  .photo-clock{left:620px;top:735px;width:555px;height:275px;background:radial-gradient(circle at 55% 50%,#ffffff 0 30%,#d7dde3 55%,#9aa4ae)}
  .photo-solution{left:620px;top:1640px;width:555px;height:255px;background:linear-gradient(135deg,#ffffff,#cfe2f3 55%,#7eaedc)}
  .tip-head{position:absolute;display:flex;align-items:stretch;min-height:76px}
  .tip-left{left:25px;width:562px}
  .tip-right{left:620px;width:555px}
  .tip-num{
    flex:0 0 110px;background:var(--blue-dark);color:var(--white);
    font-family:"Roboto",sans-serif;font-weight:700;font-size:56px;
    display:flex;align-items:center;justify-content:center;
  }
  .tip-title{
    flex:1;background:var(--blue);color:var(--white);
    font-weight:600;font-size:36px;line-height:1.1;padding:10px 20px;
    display:flex;align-items:center;
  }
  .tip-body{position:absolute;font-size:15.5px;line-height:1.45}
  .body-left{left:40px;width:535px}
  .body-right{left:635px;width:530px}
  .footer{
    position:absolute;left:0;top:2970px;width:1200px;height:205px;background:var(--slate);
    color:var(--white);text-align:center;display:flex;flex-direction:column;justify-content:center;
    font-weight:700;font-size:36px;line-height:1.3;
  }
</style>
</head>
<body>
  <header class="masthead">
    <span class="brand-name">Pendrake Tax</span><span class="brand-mark"></span>
  </header>
  <div class="title-band"><h1>How to survive a<br>Tax Investigation</h1></div>
  <div class="spine"></div>

  <!-- left column -->
  <div class="photo photo-kneeling" role="img" aria-label="Photo of a businessman in a suit kneeling with his head bowed to the floor"></div>
  <div class="tip-head tip-left" style="top:672px"><div class="tip-num">01</div><div class="tip-title">Don’t Panic</div></div>
  <p class="tip-body body-left" style="top:765px">For many here will be an initial knee jerk reaction such as fear, denial and anger or a desire to have a chat with the Inspector to show you are a good person and willing to help or to assure BQTF there is nothing wrong. This is a time for cool heads, planning and contemplation as to what could be the problems and taking stock of the situation. Do not do anything rash and:</p>

  <div class="photo photo-card" role="img" aria-label="Photo of a hand holding out a business card"></div>
  <div class="tip-head tip-left" style="top:1372px"><div class="tip-num">02</div><div class="tip-title">Take Expert advice</div></div>
  <p class="tip-body body-left" style="top:1465px">Your first discussion may be with your accountant. Some are good at tax investigation work, many are not specialists. Engaging a specialist can make all the difference in time taken to deal with the issues and the eventual outcome. You must have an open and honest conversation about what may or may not have gone on and sometimes this is difficult with existing advisors. An expert in the field of tax investigations understands the legal frame work in which BQTF operates and the subtleties of tax investigations which can be used to your advantage. After all you would not ask a GP to conduct specialised surgery.</p>

  <div class="tip-head tip-left" style="top:1745px"><div class="tip-num">03</div><div class="tip-title">Don’t Lie</div></div>
  <p class="tip-body body-left" style="top:1838px">Tell your advisor the truth, if you have chosen well then they will be able to manage the situation properly. If there is something wrong then it is best this is disclosed to BQTF at the earliest given opportunity.</p>

  <div class="tip-head tip-left" style="top:1962px"><div class="tip-num">04</div><div class="tip-title">BQTF already<br>knows quite a lot</div></div>
  <p class="tip-body body-left" style="top:2095px">BQTF rarely go on ‘fishing expeditions’. Before any tax investigation they review your tax returns and research their ‘data warehouse’ for background information on property and other assets, interest bearing bank accounts and now they have access to various information from Q5 countries including overseas property. Often they will have sufficient evidence to suspect that there are problems with your tax affairs. If you do not tell them and they have to tell you then the costs of sorting the matter out goes up significantly.</p>

  <div class="tip-head tip-left" style="top:2360px"><div class="tip-num">05</div><div class="tip-title">Think critically</div></div>
  <p class="tip-body body-left" style="top:2452px">Think about what has gone wrong (if it has) and how it has happened. Before sending anything to BQTF make sure it has been looked at and consider if anything needs explanation. Make sure if any bank statements are sent to BQTF that any non-business deposits are explained.</p>

  <div class="tip-head tip-left" style="top:2632px"><div class="tip-num">06</div><div class="tip-title">Prepare for meetings</div></div>
  <p class="tip-body body-left" style="top:2725px">If you do attend a meeting make sure you are prepared. Anticipate any questions (this is where an experienced advisor really helps) and think about your answers. Never attend without an advisor and ensure you take notes of what was said. Meetings are not just about finding more about the business, they are designed to catch you out.</p>

  <!-- right column -->
  <div class="tip-head tip-right" style="top:378px"><div class="tip-num">07</div><div class="tip-title">Question what BQTF<br>are asking for</div></div>
  <p class="tip-body body-right" style="top:505px">BQTF often ask for things that they are not entitled to or send out onerous requests. Ask them why they need the information and think about what it has to do with your tax affairs. If the answer is it is nothing to do with your tax return then it is unlikely that it should be provided.</p>

  <div class="photo photo-clock" role="img" aria-label="Photo of a clock face with a red second hand"></div>
  <div class="tip-head tip-right" style="top:1020px"><div class="tip-num">08</div><div class="tip-title">Deadline<br>Management</div></div>
  <p class="tip-body body-right" style="top:1140px">BQTF Officers are under tremendous internal pressure to keep Investigations flowing. They will often suggest deadlines for the provision of information and responses. Often these are unreasonable. If you think they are entitled to the information then think about how long it will take you to do as they ask. Then tell them how long you think it will take to do. Remember where there are delays BQTF have unavoidable delays due to pressure of work, you are not cooperating!</p>

  <div class="tip-head tip-right" style="top:1372px"><div class="tip-num">09</div><div class="tip-title">Make Payments<br>on Account</div></div>
  <p class="tip-body body-right" style="top:1495px">If you do owe tax then (if you have the funds) you should make payments on account to BQTF. This demonstrates cooperation with BQTF and stops the clock of further interest accruing from the date the payment is made on the amount of the payment.</p>

  <div class="photo photo-solution" role="img" aria-label="Photo of a finger touching the word Solution on a bright screen"></div>
  <div class="tip-head tip-right" style="top:1915px"><div class="tip-num">10</div><div class="tip-title">Find Solutions</div></div>
  <p class="tip-body body-right" style="top:2005px">At certain points in a tax investigation there will be questions to which no one knows the answer or technical ‘grey’ areas where the answer is unclear. Make pragmatic suggestions to BQTF as to how these could be resolved.</p>

  <div class="tip-head tip-right" style="top:2115px"><div class="tip-num">11</div><div class="tip-title">Mitigate Penalties /<br>Name and Shame</div></div>
  <p class="tip-body body-right" style="top:2240px">Penalties are based on perceived behaviour so make sure you understand how these work and read BQTF’s own guidance on this. Ensure that all answers to questions support the behaviour that you think has happened and that the penalty mitigation factors have all been covered. The difference between disclosing problems and helping sort them out, or denying them can reduce penalties by a massive margin. Behaviour during the enquiry can also have an influence on whether you appear on the quarterly name and shame list of “tax cheats” or not. Make sure you are not.</p>

  <div class="tip-head tip-right" style="top:2545px"><div class="tip-num">12</div><div class="tip-title">Don’t Do It Again!</div></div>
  <p class="tip-body body-right" style="top:2640px">BQTF do not look favourably on second time offenders and at best they will charge you a high penalty and these are always looked at more seriously for prosecution. Tax investigations are such a traumatic experience that most people never want to experience them again.</p>

  <footer class="footer">
    <p>For professional advice on tax investigation<br>please contact Pendrake Tax</p>
    <p>www.pendraketax.co.uk Telephone: 0113 496 0731</p>
  </footer>
</body>
</html>
```